Tile installation contractor -business card design

We are a tile contractor doing installation of tile on floors, walls, we tile showers, backsplashes, kitchens, entry ways. we install all types of tile ceramic, porcelain, travertine, marble, slate ect. we also do demolition and tear outs of old existing tile (removal) we do commercial, or residential jobs. tile and grout repairs. sealing of grout/tile. small or large jobs. we are fast, clean, do quality work, honest and hard working. anything tile we can do. design or patterns. we do shower pans and all prep work needed to install tile. fair competitive pricing
Industry/Entity Type
Business
Contact Information for Business Card
Bramblecrest Tile- company name
Dale Kroner/ owner 801-555-2936
bramblecrest_tile@quillmail.test
Free Estimates
Larkfield Utah, 84099
20+ years experience
Licensed and Insured

```html
<!DOCTYPE html>
<html lang="en">
<head>
<meta charset="UTF-8">
<title>Bramblecrest Tile – Business Card</title>
<link rel="stylesheet" href="https://fonts.googleapis.com/css2?family=Lato:wght@300;400&family=Nunito:wght@800&display=swap">
<style>
  :root {
    --navy: #1a2134;
    --sand: #c3b6a1;
    --sand-text: #cbbda6;
    --muted: #8e8c8c;
    --backdrop: #ecebea;
    --photo-warm: #c49a5a;
    --photo-cool: #9a9a94;
  }
  * { box-sizing: border-box; margin: 0; padding: 0; }
  html, body {
    width: 1200px; height: 863px; overflow: hidden;
    background: var(--backdrop);
  }
  .canvas {
    position: relative; width: 1200px; height: 863px;
    display: flex; justify-content: center; align-items: center; gap: 60px;
  }
  .card {
    position: relative; width: 300px; height: 525px; overflow: hidden;
    box-shadow: 0 10px 30px rgba(0,0,0,0.18);
  }

  /* Front */
  .card-front { background: var(--sand); font-family: "Lato", sans-serif; }
  .side-tab {
    position: absolute; top: 70px; width: 16px; height: 190px;
    background: var(--navy); border-radius: 10px;
  }
  .side-tab.left { left: 12px; }
  .side-tab.right { right: 12px; }
  .project-photo {
    position: absolute; top: 40px; left: 36px; width: 228px; height: 190px;
    border-radius: 20px;
    background: linear-gradient(160deg, var(--photo-cool) 0%, var(--photo-warm) 45%, #b88a4c 70%, var(--photo-cool) 100%);
  }
  .band {
    position: absolute; left: 0; width: 100%;
    display: flex; align-items: center; justify-content: center;
    font-size: 17px; letter-spacing: 0.5px; text-transform: uppercase;
  }
  .band.dark { background: var(--navy); color: var(--sand-text); }
  .band.light { color: var(--navy); }
  .band-experience { top: 245px; height: 55px; }
  .band-estimates { top: 300px; height: 52px; }
  .band-licensed { top: 357px; height: 60px; }

  /* Back */
  .card-back { background: var(--navy); font-family: "Lato", sans-serif; }
  .accent-bar {
    position: absolute; left: -6px; top: 60px; width: 18px; height: 235px;
    background: var(--sand); border-radius: 10px;
  }
  .contact { position: absolute; left: 36px; top: 82px; right: 16px; }
  .company-name {
    font-family: "Nunito", sans-serif; font-weight: 800;
    font-size: 22px; color: var(--sand-text); margin-bottom: 22px;
  }
  .meta { font-weight: 300; font-size: 13px; color: var(--muted); line-height: 1.35; }
  .person { margin-top: 22px; }
  .person-name { font-size: 16px; color: var(--sand-text); }
  .person-role { font-weight: 300; font-size: 14px; color: var(--muted); }
  .person-phone { font-weight: 300; font-size: 14px; color: var(--muted); }
</style>
</head>
<body>
<main class="canvas">
  <section class="card card-front">
    <div class="side-tab left"></div>
    <div class="side-tab right"></div>
    <div class="project-photo" role="img" aria-label="Photo of a finished tiled bathroom with a soaking tub and mosaic floor inlay"></div>
    <div class="band dark band-experience">20+ Years Experience</div>
    <div class="band light band-estimates">Free Estimates</div>
    <div class="band dark band-licensed">Licensed and Ensured</div>
  </section>

  <section class="card card-back">
    <div class="accent-bar"></div>
    <div class="contact">
      <h1 class="company-name">Bramblecrest Tile</h1>
      <p class="meta">bramblecrest_tile@quillmail.test<br>Larkfield Utah, 84099</p>
      <div class="person">
        <p class="person-name">Dale Kroner <span class="person-role">/Owner</span></p>
        <p class="person-phone">801-555-2936</p>
      </div>
      <div class="person">
        <p class="person-name">Reid Halvorsen</p>
        <p class="person-phone">801-555-4170</p>
      </div>
    </div>
  </section>
</main>
</body>
</html>
```